stars + comments Reviews website design (similar to grubly concept)

Please refer to attached logo and wire frames
----------------------------------------------------------------------------------------------------
we are a company based in egypt, seeking a design for a website that allows user to find doctors using search and filters.
also it allows user to review this doctor through providing comment and 1 to 5 stars
i need 4 main pages designs:
1- Doctors list/favorites list
2- Doctor view
3- Add doctor (3 steps)
4- Sign-in/sign up
5- Menu design
am into the colors teal/turquoise (though am open for different opinion)
i don't want the design theme to be doctors specific
am into the school of very clean, very neat, very simple
(chirpnet, pagecircle, snapmosaic designs are appealing to me)
Updates

Number of Pages Required

4 page

Font styles to use
Sans Serif

Colors
00a990
33b8a4

Requirements
Must have
• website will be bilingual/ bi-directional (English and Arabic)
• designer needs to provide another copy of the design with "right to left" orientation
• interactive button animation

```html
<!DOCTYPE html>
<html lang="en">
<head>
<meta charset="utf-8">
<title>Revuly – Doctors</title>
<link href="https://fonts.googleapis.com/css2?family=Roboto:ital,wght@0,300;0,400;0,500;1,300;1,400&display=swap" rel="stylesheet">
<style>
:root{
  --teal:#00a990;
  --teal-light:#33b8a4;
  --teal-dark:#0d8c7e;
  --ink:#222;
  --muted:#555;
  --line:#d6d6d6;
  --page:#f4f4f2;
  --footer:#efefef;
  --star:#f7c21a;
  --btn:#2b2b2b;
}
*{box-sizing:border-box;margin:0;padding:0}
html,body{width:1200px;height:934px;overflow:hidden}
body{font-family:'Roboto',sans-serif;background:var(--page);color:var(--ink);position:relative}

.site-header{position:absolute;left:0;top:0;width:1200px;height:69px;background:linear-gradient(180deg,#3cbfad 0%,var(--teal) 60%,#0a9a86 100%);border-bottom:2px solid var(--teal-dark)}
.brand{position:absolute;left:75px;top:16px;display:flex;align-items:center;gap:8px;color:#fff;font-size:30px;font-weight:400}
.brand-dot{width:22px;height:22px;border-radius:50%;background:#fff}
.main-nav{position:absolute;left:640px;top:0;height:67px;display:flex}
.nav-item{height:67px;display:flex;flex-direction:column;align-items:center;justify-content:center;gap:5px;color:#fff;font-size:11px;font-weight:500;letter-spacing:.4px;padding:0 25px;border-right:1px solid rgba(255,255,255,.2)}
.nav-item svg{width:18px;height:18px;fill:#fff}
.user-menu{position:absolute;left:917px;top:16px;display:flex;align-items:center;gap:12px;color:#fff;font-size:11.5px;font-weight:500}
.avatar{width:38px;height:38px;border-radius:50%;background:linear-gradient(135deg,#8c6d55,#3e3b38);border:2px solid #e6f6f3}
.caret{width:0;height:0;border-left:5px solid transparent;border-right:5px solid transparent;border-top:5px solid #fff}
.user-menu::after{content:"";position:absolute;right:-20px;top:-16px;height:67px;border-right:1px solid rgba(255,255,255,.2)}
.lang{position:absolute;left:1087px;top:29px;font-size:11px;color:#fff;font-weight:500}
.lang b{color:#113;font-weight:500}

.filter-bar{position:absolute;left:0;top:71px;width:1200px;height:69px;background:#fff;border-bottom:1px solid #e2e2e2}
.field{position:absolute;top:19px;width:163px;height:30px;border:1px solid var(--line);background:#fff;font-size:11px;font-style:italic;font-weight:300;color:#777;padding:9px 12px}
.field .end{position:absolute;right:0;top:0;width:32px;height:28px;border-left:1px solid var(--line);display:flex;align-items:center;justify-content:center}
.field .end .caret{border-top-color:var(--teal)}

.results{position:absolute;left:209px;top:173px;width:781px;display:flex;justify-content:space-between;align-items:baseline}
.results h1{font-size:17px;font-weight:400;color:var(--teal);letter-spacing:.3px}
.results p{font-size:13px;font-style:italic;font-weight:300;color:#333}
.results p span{font-weight:400}

.doctor-card{position:absolute;left:209px;width:781px;height:127px;background:#fff;border:1px solid var(--line)}
.photo{position:absolute;left:20px;top:19px;width:84px;height:84px}
.name{position:absolute;left:124px;top:16px;font-size:17px;color:var(--teal)}
.name small{font-size:13px;color:#444;font-weight:300;margin-left:4px}
.meta{position:absolute;left:124px;top:43px;font-size:13px;color:#111}
.meta a{color:var(--teal-light);text-decoration:none;font-weight:300;margin-left:10px}
.meta i{font-style:normal;margin-left:8px}
.bio{position:absolute;left:124px;top:70px;width:420px;font-size:12.6px;line-height:19.5px;color:#555;font-weight:300}
.reviews{position:absolute;left:611px;top:18px;font-size:12.5px;font-style:italic;font-weight:300;color:#333}
.rating{position:absolute;left:611px;top:42px;display:flex;align-items:center;gap:1px}
.rating svg{width:18px;height:18px}
.rating span{margin-left:14px;font-size:13px;color:#222}
.like{position:absolute;left:611px;top:82px;width:19px;height:18px}

.load-more{position:absolute;left:546px;top:789px;width:108px;height:33px;background:var(--btn);color:#fff;font-size:13px;font-weight:500;letter-spacing:.3px;display:flex;align-items:center;justify-content:center;border-radius:2px;transition:background .2s}
.load-more:hover{background:var(--teal)}

.site-footer{position:absolute;left:0;top:847px;width:1200px;height:87px;background:var(--footer)}
.copyright{position:absolute;left:75px;top:38px;font-size:11.5px;color:#555;font-weight:300}
.social{position:absolute;right:75px;top:34px;display:flex;gap:12px;font-size:10.5px;color:#555}
.social span{display:flex;align-items:center;gap:4px}
.social i{width:18px;height:18px;border-radius:50%;background:var(--teal-dark)}
</style>
</head>
<body>
<header class="site-header">
  <div class="brand"><span class="brand-dot"></span>Revuly</div>
  <nav class="main-nav">
    <div class="nav-item"><svg viewBox="0 0 24 24"><path d="M12 3 2 12h3v9h5v-6h4v6h5v-9h3z"/></svg>HOME</div>
    <div class="nav-item"><svg viewBox="0 0 24 24"><path d="M12 21 3.5 12.5A5 5 0 0 1 12 6a5 5 0 0 1 8.5 6.5z"/></svg>LIKES</div>
    <div class="nav-item"><svg viewBox="0 0 24 24"><circle cx="9" cy="8" r="4"/><path d="M2 22c0-5 3-8 7-8s7 3 7 8z"/><rect x="15" y="1" width="8" height="8" rx="1"/><path d="M18.5 2.5h1v2h2v1h-2v2h-1v-2h-2v-1h2z" fill="#00a990"/></svg>DOCTORS</div>
  </nav>
  <div class="user-menu"><span class="avatar" role="img" aria-label="User profile photo"></span>SAM ROWE<span class="caret"></span></div>
  <div class="lang"><b>EN</b> / AR</div>
</header>

<section class="filter-bar">
  <div class="field" style="left:75px">Search...<span class="end"><svg width="14" height="14" viewBox="0 0 14 14"><circle cx="5.5" cy="5.5" r="4" fill="none" stroke="#0d8c7e" stroke-width="2"/><path d="M8.5 8.5 13 13" stroke="#0d8c7e" stroke-width="2.4"/></svg></span></div>
  <div class="field" style="left:253px">Specialization<span class="end"><span class="caret"></span></span></div>
  <div class="field" style="left:430px">Sub-Specialization<span class="end"><span class="caret"></span></span></div>
  <div class="field" style="left:607px">Select Area<span class="end"><span class="caret"></span></span></div>
  <div class="field" style="left:785px">Select Gender<span class="end"><span class="caret"></span></span></div>
  <div class="field" style="left:963px">Select Rating<span class="end"><span class="caret"></span></span></div>
</section>

<svg width="0" height="0" style="position:absolute">
  <defs>
    <path id="star" d="M9 1l2.4 5 5.4.7-4 3.8 1 5.4L9 13.3 4.2 15.9l1-5.4-4-3.8 5.4-.7z"/>
    <linearGradient id="half"><stop offset="50%" stop-color="#f7c21a"/><stop offset="50%" stop-color="#fff"/></linearGradient>
    <path id="heart" d="M9.5 16.5 2.3 9.6A4.2 4.2 0 0 1 9.5 4a4.2 4.2 0 0 1 7.2 5.6z"/>
  </defs>
</svg>

<div class="results"><h1>DOCTORS</h1><p>Results Found: <span>15, 123 Doctors</span></p></div>

<article class="doctor-card" style="top:207px">
  <div class="photo" role="img" aria-label="Portrait of a female doctor in teal scrubs" style="background:linear-gradient(135deg,#d9a84a,#3aa9a0)"></div>
  <div class="name">Omar Hady<small>(1km&nbsp; away)</small></div>
  <div class="meta">Anesthesiologist<i>|</i><a>12 Nile View Street,Dokki</a></div>
  <p class="bio">Lorem ipsum dolor sit amet, consectetur adipisicing eitseo eiusmod tempor incididunt ut labore et dolore magna aliqua...</p>
  <div class="reviews">Reviews :</div>
  <div class="rating"><svg viewBox="0 0 18 17"><use href="#star" fill="#f7c21a"/></svg><svg viewBox="0 0 18 17"><use href="#star" fill="#f7c21a"/></svg><svg viewBox="0 0 18 17"><use href="#star" fill="#f7c21a"/></svg><svg viewBox="0 0 18 17"><use href="#star" fill="#f7c21a"/></svg><svg viewBox="0 0 18 17"><use href="#star" fill="url(#half)" stroke="#f7c21a" stroke-width="1.2"/></svg><span>(123)</span></div>
  <svg class="like" viewBox="0 0 19 18"><use href="#heart" fill="none" stroke="#0d8c7e" stroke-width="2"/></svg>
</article>

<article class="doctor-card" style="top:349px">
  <div class="photo" role="img" aria-label="Portrait of a male doctor with stethoscope" style="background:linear-gradient(135deg,#c9b39a,#e8edf1)"></div>
  <div class="name">Omar Hady<small>(1km&nbsp; away)</small></div>
  <div class="meta">Anesthesiologist<i>|</i><a>12 Nile View Street,Dokki</a></div>
  <p class="bio">Lorem ipsum dolor sit amet, consectetur adipisicing eitseo eiusmod tempor incididunt ut labore et dolore magna aliqua...</p>
  <div class="reviews">Reviews :</div>
  <div class="rating"><svg viewBox="0 0 18 17"><use href="#star" fill="#f7c21a"/></svg><svg viewBox="0 0 18 17"><use href="#star" fill="#f7c21a"/></svg><svg viewBox="0 0 18 17"><use href="#star" fill="#f7c21a"/></svg><svg viewBox="0 0 18 17"><use href="#star" fill="#f7c21a"/></svg><svg viewBox="0 0 18 17"><use href="#star" fill="url(#half)" stroke="#f7c21a" stroke-width="1.2"/></svg><span>(123)</span></div>
  <svg class="like" viewBox="0 0 19 18"><use href="#heart" fill="#0d8c7e"/></svg>
</article>

<article class="doctor-card" style="top:492px">
  <div class="photo" role="img" aria-label="Portrait of a smiling male doctor in a white coat" style="background:linear-gradient(135deg,#dfe6ea,#5a4436)"></div>
  <div class="name">Omar Hady<small>(1km&nbsp; away)</small></div>
  <div class="meta">Anesthesiologist<i>|</i><a>12 Nile View Street,Dokki</a></div>
  <p class="bio">Lorem ipsum dolor sit amet, consectetur adipisicing eitseo eiusmod tempor incididunt ut labore et dolore magna aliqua...</p>
  <div class="reviews">Reviews :</div>
  <div class="rating"><svg viewBox="0 0 18 17"><use href="#star" fill="#f7c21a"/></svg><svg viewBox="0 0 18 17"><use href="#star" fill="#f7c21a"/></svg><svg viewBox="0 0 18 17"><use href="#star" fill="#f7c21a"/></svg><svg viewBox="0 0 18 17"><use href="#star" fill="#f7c21a"/></svg><svg viewBox="0 0 18 17"><use href="#star" fill="url(#half)" stroke="#f7c21a" stroke-width="1.2"/></svg><span>(123)</span></div>
  <svg class="like" viewBox="0 0 19 18"><use href="#heart" fill="none" stroke="#0d8c7e" stroke-width="2"/></svg>
</article>

<article class="doctor-card" style="top:636px">
  <div class="photo" role="img" aria-label="Portrait of a senior male doctor with arms crossed" style="background:linear-gradient(135deg,#f1f1f1,#c8b7a6)"></div>
  <div class="name">Omar Hady<small>(1km&nbsp; away)</small></div>
  <div class="meta">Anesthesiologist<i>|</i><a>12 Nile View Street,Dokki</a></div>
  <p class="bio">Lorem ipsum dolor sit amet, consectetur adipisicing eitseo eiusmod tempor incididunt ut labore et dolore magna aliqua...</p>
  <div class="reviews">Reviews :</div>
  <div class="rating"><svg viewBox="0 0 18 17"><use href="#star" fill="#f7c21a"/></svg><svg viewBox="0 0 18 17"><use href="#star" fill="#f7c21a"/></svg><svg viewBox="0 0 18 17"><use href="#star" fill="#f7c21a"/></svg><svg viewBox="0 0 18 17"><use href="#star" fill="#f7c21a"/></svg><svg viewBox="0 0 18 17"><use href="#star" fill="url(#half)" stroke="#f7c21a" stroke-width="1.2"/></svg><span>(123)</span></div>
  <svg class="like" viewBox="0 0 19 18"><use href="#heart" fill="none" stroke="#0d8c7e" stroke-width="2"/></svg>
</article>

<div class="load-more">LOAD MORE</div>

<footer class="site-footer">
  <p class="copyright">Copyright ©2015.Company Name. All Right Reserved &nbsp;|&nbsp; Privacy Policy</p>
  <div class="social">
    <span><i></i>pagecircle</span>
    <span><i></i>chirpnet</span>
    <span><i></i>snapmosaic</span>
  </div>
</footer>
</body>
</html>
```